Looking for a tri-fold flyer for a new energy conservation company

We are a locally owned energy conservation company that focuses on making energy efficiency upgrades to residential, commercial, and agricultural properties. Services range from solar, re-roofs, dual pane windows, HVAC's, tankless water heaters, water efficient products, I have a list of items I can upload to show all services and pictures of a website that we are building currently. I would like the tri fold to include who, what, why info I have attached. I would like to see a modern design with Bold Capitalized text, our blue color to be used a lot with the green maybe accent colors.

Target Market(s)

please see attachment

Industry/Entity Type

It Company

Requirements
Must have
• please see attachment
Nice to have
• please see attachment
Should not have
• Colors requested below are in the logo that is attached as a PSD file.

```html
<!DOCTYPE html>
<html lang="en">
<head>
<meta charset="utf-8">
<title>Brightleaf Builders Tri-fold</title>
<link rel="stylesheet" href="https://fonts.googleapis.com/css2?family=Josefin+Sans:wght@400;600;700&family=Arimo:wght@400;700&display=swap">
<style>
:root{
  --bg:#a9c9e3;
  --blue:#1598e0;
  --blue-deep:#0a7fcc;
  --strip:#ecebe8;
  --green:#6bb52b;
  --green-light:#9ed45a;
  --ink:#5d5d5d;
  --white:#ffffff;
}
*{box-sizing:border-box;margin:0;padding:0}
html,body{width:977px;height:1200px;overflow:hidden;background:var(--bg)}
body{position:relative;font-family:"Arimo",Arial,sans-serif;color:var(--ink)}
.spread{position:absolute;left:128px;width:720px;height:560px;display:flex;box-shadow:0 10px 30px rgba(0,40,80,.25)}
.spread--inside{top:20px}
.spread--outside{top:620px}
.panel{position:relative;width:240px;height:100%;background:linear-gradient(180deg,var(--blue),var(--blue-deep));overflow:hidden}
.strip{position:absolute;top:0;bottom:0;background:var(--strip)}
.heading{font-family:"Josefin Sans",sans-serif;font-weight:600;color:var(--green);text-transform:uppercase;letter-spacing:1px}
.body-copy{font-size:11.4px;line-height:14.6px}
.rule{height:1px;background:#c9c9c6;margin:0 auto}
.ring{position:absolute;border-radius:50%;background:var(--strip);border:9px solid var(--green);box-shadow:0 0 0 3px var(--green-light) inset,0 3px 8px rgba(0,0,0,.2);display:flex;flex-direction:column;align-items:center;justify-content:center;text-align:center}
.ring .big{font-family:"Josefin Sans",sans-serif;font-weight:700;color:var(--green);font-size:36px;line-height:32px}
.ring .small{font-family:"Josefin Sans",sans-serif;color:var(--green);font-size:22px;line-height:22px}
.photo{position:absolute}
/* inside left */
.about{left:10px;width:188px}
.about .heading{position:absolute;top:60px;left:14px;font-size:28px}
.about .heading span{font-weight:400}
.about .body-copy{position:absolute;top:112px;left:12px;width:166px}
.about .rule{position:absolute;top:402px;left:20px;width:150px}
.about .photo{left:0;right:0;top:410px;height:118px;background:linear-gradient(135deg,#3e5e3a,#8a7a6a 55%,#d8d2cc)}
/* inside middle */
.offer{left:36px;width:168px}
.offer .ring{left:-8px;top:18px;width:184px;height:184px}
.offer .body-copy{position:absolute;top:232px;left:12px;width:150px;color:#6e6e6e}
.feature{position:absolute;left:14px;display:flex;align-items:center;gap:6px}
.feature .icon{width:44px;height:44px;border-radius:50%;background:var(--green);display:flex;align-items:center;justify-content:center}
.feature .label{font-family:"Josefin Sans",sans-serif;font-size:9px;line-height:9px;letter-spacing:1px;text-transform:uppercase;color:#8a8a8a}
.feature .label b{color:var(--green);font-size:10.5px;font-weight:600;display:block;line-height:10px}
.offer .rule{position:absolute;left:14px;width:140px}
/* inside right */
.sectors{left:36px;width:176px}
.sector{position:absolute;left:0;width:176px;text-align:center}
.sector .icon{width:56px;height:56px;border-radius:50%;background:var(--green);margin:0 auto 6px;display:flex;align-items:center;justify-content:center}
.sector .heading{font-size:14px;letter-spacing:1.2px;margin-bottom:3px}
.sector p{font-size:7.6px;line-height:9.6px;text-align:left;padding:0 24px 0 30px;color:#6a6a6a}
/* outside left */
.cover{left:46px;width:150px}
.cover .ring{left:-24px;top:202px;width:198px;height:198px}
.brand-name{font-family:"Arimo",Arial,sans-serif;font-weight:700;color:var(--green);font-size:22px;line-height:24px}
.cover .tagline{position:absolute;left:10px;top:430px;width:136px;font-family:"Josefin Sans",sans-serif;font-weight:700;color:var(--blue);font-size:15.5px;line-height:15px;text-transform:uppercase;letter-spacing:1px}
.cover .rule{position:absolute;width:120px;left:14px}
/* outside middle */
.back .brand-name{position:absolute;bottom:54px;left:0;right:0;text-align:center;color:var(--white);font-size:16px}
/* outside right */
.who .photo{left:46px;width:150px;top:0;height:190px;background:linear-gradient(180deg,#6b5a4a,#3a2e24 60%,#2a231c);border:3px solid var(--strip);border-top:none}
.who .ring{left:44px;top:150px;width:152px;height:152px}
.who .ring .big{font-size:28px;line-height:26px}
.who .ring .small{font-size:18px}
.who .brand-name{position:absolute;top:322px;left:30px;width:190px;color:var(--white);font-size:20px}
.who .body-copy{position:absolute;top:354px;left:30px;width:186px;color:var(--white);font-size:11.4px}
</style>
</head>
<body>
<section class="spread spread--inside" aria-label="Inside spread">
  <div class="panel">
    <div class="strip about">
      <h2 class="heading">About<span>Us</span></h2>
      <p class="body-copy"><b>Brightleaf Builders</b> is a local company in Maple Valley, CA with over 25 years of experience in all aspects of construction. We are the only business that specializes in total home and business energy conservation. We offer detailed financial analysis of all considered improvements to ensure you make the best decision possible. We pride ourselves in providing exceptional service, quality products, and competitive pricing. These core values set us apart from other providers in our industry, and we look forward to working with you.</p>
      <div class="rule"></div>
      <div class="photo" role="img" aria-label="Photo of the team standing together outdoors"></div>
    </div>
  </div>
  <div class="panel">
    <div class="strip offer">
      <div class="ring"><span class="big">WHAT</span><span class="small">WE OFFER</span></div>
      <p class="body-copy">Brightleaf Builders will provide our customers comfort all year round by reducing energy usage and utility bills; saving you money. Making such improvements increases the value of your home and adds even greater curb appeal.</p>
      <div class="rule" style="top:372px"></div>
      <div class="feature" style="top:382px">
        <div class="icon"><svg width="28" height="24" viewBox="0 0 28 24"><rect x="2" y="2" width="24" height="13" fill="none" stroke="#fff" stroke-width="2"/><path d="M10 2v13M18 2v13M2 8.5h24M14 15v7M9 22h10" stroke="#fff" stroke-width="2" fill="none"/></svg></div>
        <div class="label"><b>Best</b><b>Available</b>Energy efficient<br>products</div>
      </div>
      <div class="feature" style="top:442px">
        <div class="icon"><svg width="24" height="30" viewBox="0 0 24 30"><path d="M18 8c-1-2-3.5-3-6-3-3.5 0-6 1.8-6 4.5 0 6 12 3 12 9.5 0 2.8-2.7 4.5-6 4.5-3 0-5.5-1.3-6.5-3.5M12 1v28" stroke="#fff" stroke-width="3" fill="none"/></svg></div>
        <div class="label"><b>Competitive</b><b>Pricing</b>Options for our<br>customers</div>
      </div>
      <div class="rule" style="top:496px"></div>
    </div>
  </div>
  <div class="panel">
    <div class="strip sectors">
      <div class="sector" style="top:24px">
        <div class="icon"><svg width="32" height="28" viewBox="0 0 32 28"><path d="M3 14L16 3l13 11" stroke="#fff" stroke-width="3" fill="none"/><path d="M7 13v13h7v-8h4v8h7V13" fill="#fff"/></svg></div>
        <h3 class="heading">Residential</h3>
        <p>Our residential solar solutions can help reduce your energy cost with the most cost effective approach and most efficient panels on the market.</p>
      </div>
      <div class="sector" style="top:196px">
        <div class="icon"><svg width="30" height="32" viewBox="0 0 30 32"><rect x="3" y="8" width="11" height="22" fill="#fff"/><rect x="16" y="2" width="11" height="28" fill="#fff"/><path d="M6 12h5M6 17h5M6 22h5M19 7h5M19 12h5M19 17h5M19 22h5" stroke="#6bb52b" stroke-width="2"/></svg></div>
        <h3 class="heading">Commercial</h3>
        <p>Our commercial solar solutions include private and public sectors for schools, hospitals, government bodies, churches, retail stores and private business owners, which will lock in your energy cost for years to come and reduce your operating costs.</p>
      </div>
      <div class="sector" style="top:394px">
        <div class="icon"><svg width="30" height="30" viewBox="0 0 30 30"><path d="M5 25C5 12 13 5 26 4c0 13-7 21-20 21z" fill="#fff"/><path d="M5 25L18 12" stroke="#6bb52b" stroke-width="2"/></svg></div>
        <h3 class="heading">Agriculture</h3>
        <p>Our agricultural solar solutions are a must for Ag businesses that plan operations and expenditures years in advance to remain competitive in an increasingly global food economy.</p>
      </div>
    </div>
  </div>
</section>

<section class="spread spread--outside" aria-label="Outside spread">
  <div class="panel">
    <div class="strip cover">
      <div class="ring"><span class="brand-name">Brightleaf</span><span class="brand-name" style="font-size:15px">Builders</span></div>
      <div class="rule" style="top:418px"></div>
      <p class="tagline">Your local renovation &amp; conservation specialist</p>
      <div class="rule" style="top:510px"></div>
    </div>
  </div>
  <div class="panel back">
    <p class="brand-name">Brightleaf Builders</p>
  </div>
  <div class="panel who">
    <div class="photo" role="img" aria-label="Photo of hands holding soil with a young green seedling"></div>
    <div class="ring"><span class="big">WHO</span><span class="small">WE ARE</span></div>
    <p class="brand-name">Brightleaf Builders</p>
    <p class="body-copy">is your all-in-one energy conservation improvement contractor. We help homeowners, business owners, and the private sector reduce energy costs while reducing their carbon footprint.</p>
  </div>
</section>
</body>
</html>
```